New Flyer Design Project

Hi,
We were looking at a flyer for the testing run of the event. I have attached a design we like with comments on what to remove and add. Also attached is our logo. We want something with the same style and feel of the flyer attached and it suited the event we are running.
Thanks,
Colin
Colors
Designer to choose colors to be used in the design.

```html
<!DOCTYPE html>
<html lang="en">
<head>
<meta charset="utf-8">
<title>The Ridge Runner – Test Run Flyer</title>
<link rel="stylesheet" href="https://fonts.googleapis.com/css2?family=Michroma&family=Oswald:wght@500&family=Montserrat:wght@600;800&display=swap">
<style>
  :root {
    --page: #ffffff;
    --sky-top: #5e8c74;
    --sky-mid: #a9bf92;
    --sky-low: #dcdfb2;
    --hill: #6d7a3e;
    --hill-deep: #3a4a22;
    --ground: #1c2611;
    --ink: #15190f;
    --accent: #ef7b2c;
    --light: #ffffff;
  }
  * { margin: 0; padding: 0; box-sizing: border-box; }
  html, body {
    width: 1200px; height: 1200px; overflow: hidden;
    background: var(--page);
  }
  .flyer {
    position: absolute; left: 236px; top: 46px;
    width: 761px; height: 1076px; overflow: hidden;
  }
  .flyer__scene {
    position: absolute; inset: 0;
    background:
      radial-gradient(circle at 24% 53%, rgba(255,250,225,.85) 0, rgba(255,240,200,.25) 50px, rgba(255,240,200,0) 120px),
      linear-gradient(180deg,
        var(--sky-top) 0%,
        var(--sky-mid) 30%,
        var(--sky-low) 46%,
        var(--sky-low) 50%,
        var(--hill) 54%,
        var(--hill-deep) 72%,
        var(--ground) 100%);
  }
  .brand__mark {
    position: absolute; top: 118px; left: 50%;
    width: 112px; height: 112px; margin-left: -56px;
    border-radius: 50%;
    background: var(--ink);
  }
  .brand {
    position: absolute; left: 0; right: 0; top: 250px;
    text-align: center;
    font-family: "Michroma", sans-serif; font-weight: 400;
    color: var(--ink);
  }
  .brand__small { display: block; font-size: 24px; letter-spacing: 10px; line-height: 30px; }
  .brand__large { display: block; font-size: 34px; letter-spacing: 2px; line-height: 46px; }
  .callout {
    position: absolute; top: 420px;
    font-family: "Oswald", sans-serif; font-weight: 500;
    font-size: 36px; line-height: 40px; color: var(--ink);
    transform: scaleX(.82); transform-origin: left center;
  }
  .callout--left { left: 206px; }
  .callout--right { left: 446px; }
  .social {
    position: absolute; top: 750px; left: 0; right: 0;
    display: flex; justify-content: center; gap: 22px;
  }
  .social__item {
    display: flex; align-items: center; gap: 8px;
    font-family: "Montserrat", sans-serif; font-weight: 600;
    font-size: 15px; color: var(--light);
  }
  .social__dot {
    width: 34px; height: 34px; border-radius: 50%;
    border: 2px solid var(--light);
  }
  .event-date {
    position: absolute; top: 836px; left: 0; right: 0;
    text-align: center;
    font-family: "Montserrat", sans-serif; font-weight: 800;
    font-size: 41px; line-height: 48px; letter-spacing: 1px;
    color: var(--accent);
  }
  .venue {
    position: absolute; left: 120px; top: 904px; width: 534px; height: 62px;
  }
  .venue svg { position: absolute; inset: 0; }
  .venue__text {
    position: absolute; inset: 0;
    display: flex; align-items: center; justify-content: center;
    font-family: "Montserrat", sans-serif; font-weight: 800;
    font-size: 37px; color: var(--light);
  }
  .contact {
    position: absolute; top: 995px; left: 0; right: 0;
    text-align: center;
    font-family: "Montserrat", sans-serif; font-weight: 600;
    font-size: 18px; color: var(--light);
  }
</style>
</head>
<body>
  <main class="flyer">
    <div class="flyer__scene" role="img" aria-label="Photograph of a trail runner silhouetted on a rocky, grassy hilltop against a hazy green sky with the sun low on the horizon"></div>

    <span class="brand__mark" aria-hidden="true"></span>
    <h1 class="brand">
      <span class="brand__small">THE</span>
      <span class="brand__large">RIDGE RUNNER</span>
    </h1>

    <p class="callout callout--left">TEST RUNNERS</p>
    <p class="callout callout--right">REQUIRED</p>

    <div class="social" aria-label="Social media">
      <span class="social__item"><span class="social__dot"></span>Trailbook</span>
      <span class="social__item"><span class="social__dot"></span>Pixgram</span>
    </div>

    <p class="event-date">15TH DECEMBER 2019</p>

    <div class="venue">
      <svg width="534" height="62" viewBox="0 0 534 62" aria-hidden="true">
        <polygon points="0,0 534,0 512,62 14,62" fill="var(--accent)"/>
      </svg>
      <p class="venue__text">AT MOUNT KALLARA</p>
    </div>

    <p class="contact">Contact hello@ridgerunnerrace.com or call 0491555218</p>
  </main>
</body>
</html>
```